zSTRIDA Membership Flyer

zSTRIDA is a shoe store selling brand name sneakers like Vorn Keltro Brisk Talvan and etc. We need a flyer to promote our membership program. On this flyer we need to emphasize that people who sign up can get 20% off their entire first purchase(certain items are excluded), which is limited time offer.
The flyer is 5.5"X4.25", two sided.
On the back side, there need to be a section where customer can fill up their name, phone number and email to join the membership.
our website is www.zstridashop.example
Member benefits can also be found on the website and should be on the flyer.

Industry/Entity Type

Shoe Store

```html
<!DOCTYPE html>
<html lang="en">
<head>
<meta charset="utf-8">
<title>zSTRIDA Membership Flyer</title>
<link href="https://fonts.googleapis.com/css2?family=Londrina+Solid:wght@400;900&family=Arimo:wght@400&family=Montserrat:wght@400&display=swap" rel="stylesheet">
<style>
  :root {
    --green: #52b548;
    --orange: #f58a21;
    --ink: #111111;
    --paper: #ffffff;
    --display: "Londrina Solid", "Arial Black", sans-serif;
    --body: "Arimo", Arial, sans-serif;
    --label: "Montserrat", Arial, sans-serif;
  }
  * { box-sizing: border-box; margin: 0; padding: 0; }
  html, body { width: 1200px; height: 900px; overflow: hidden; background: var(--paper); }
  .canvas { position: relative; width: 1200px; height: 900px; }

  .side-label { position: absolute; top: 148px; font-family: "Myriad Pro", Arial, sans-serif; font-size: 27px; color: var(--ink); }
  .side-label--front { left: 68px; }
  .side-label--back { left: 628px; }

  .panel { position: absolute; top: 240px; width: 422px; height: 548px; background: var(--paper); overflow: hidden; }
  .panel--front { left: 71px; }
  .panel--back { left: 593px; }
  .panel__corners { position: absolute; inset: 0; }

  .display { font-family: var(--display); font-weight: 900; text-transform: uppercase; letter-spacing: 2px; text-align: center; position: absolute; left: 0; right: 0; }

  .program-title { top: 16px; color: var(--green); font-size: 53px; line-height: 48px; letter-spacing: 5px; left: 6px; right: 0; }
  .offer-amount { top: 194px; color: var(--orange); font-size: 98px; line-height: 92px; letter-spacing: 7px; left: 0; right: 20px; }
  .offer-scope { top: 290px; color: var(--green); font-size: 20px; letter-spacing: 1px; }
  .offer-limit { top: 321px; color: var(--orange); font-size: 40px; line-height: 44px; letter-spacing: 3px; }
  .offer-note { position: absolute; top: 364px; right: 36px; font-family: var(--body); font-size: 11px; color: var(--orange); }
  .brand-name { top: 400px; color: var(--green); font-size: 96px; line-height: 104px; letter-spacing: 3px; text-transform: none; left: 0; right: 14px; }

  .benefits-title { top: 16px; color: var(--green); font-size: 40px; letter-spacing: 4px; }
  .benefits { position: absolute; top: 74px; left: 18px; width: 386px; font-family: var(--body); font-size: 13px; line-height: 17px; color: var(--orange); }
  .benefits p { margin-bottom: 16px; }
  .benefits .marker { display: inline-block; width: 26px; }
  .join-title { top: 342px; color: var(--green); font-size: 38px; letter-spacing: 4px; }

  .signup { position: absolute; top: 407px; left: 18px; width: 380px; list-style: none; font-family: var(--label); font-size: 15px; color: var(--orange); }
  .signup li { display: flex; align-items: baseline; height: 25px; }
  .signup .field-name { width: 161px; }
  .signup .field-line { flex: 1; border-bottom: 1px dotted var(--orange); height: 12px; }

  .social { position: absolute; top: 502px; left: 205px; font-family: var(--label); font-size: 10px; color: var(--orange); line-height: 14px; }
  .social__cta { letter-spacing: 2px; }
  .social__networks { position: absolute; top: 501px; left: 358px; font-family: var(--label); font-size: 9px; line-height: 14px; color: var(--green); }
</style>
</head>
<body>
<main class="canvas">
  <div class="side-label side-label--front">Front</div>
  <div class="side-label side-label--back">Back</div>

  <section class="panel panel--front" aria-label="Flyer front">
    <svg class="panel__corners" viewBox="0 0 422 548" aria-hidden="true">
      <path d="M268 0 Q380 30 422 115 L422 0 Z" fill="var(--orange)"/>
      <path d="M295 0 Q392 30 422 95 L422 0 Z" fill="var(--green)"/>
      <path d="M0 478 Q40 530 98 548 L0 548 Z" fill="var(--orange)"/>
      <path d="M0 497 Q32 534 80 548 L0 548 Z" fill="var(--green)"/>
    </svg>
    <h1 class="display program-title">zSTRIDA<br>Membership<br>Program</h1>
    <div class="display offer-amount">20% Off</div>
    <div class="display offer-scope">Entire First Purchase*</div>
    <div class="display offer-limit">Limited Time Offer</div>
    <div class="offer-note">*Some items excluded</div>
    <div class="display brand-name">zSTRIDA</div>
  </section>

  <section class="panel panel--back" aria-label="Flyer back">
    <svg class="panel__corners" viewBox="0 0 422 548" aria-hidden="true">
      <path d="M268 0 Q380 30 422 115 L422 0 Z" fill="var(--orange)"/>
      <path d="M295 0 Q392 30 422 95 L422 0 Z" fill="var(--green)"/>
      <path d="M0 478 Q40 530 98 548 L0 548 Z" fill="var(--orange)"/>
      <path d="M0 497 Q32 534 80 548 L0 548 Z" fill="var(--green)"/>
    </svg>
    <h2 class="display benefits-title">Benefits</h2>
    <div class="benefits">
      <p>The ZSTRIDA Member Program entitles Members to the following benefits:</p>
      <p><span class="marker">a.</span>20% OFF your entire first purchase after you sign up. Certain items are excluded from this offer. Please see stores for details.</p>
      <p><span class="marker">b.</span>10% OFF every purchase while being a member. Certain items are excluded from this offer. Please see stores for details.</p>
      <p><span class="marker">c.</span>Additional 10% OFF and FREE SHIPPING when an item is out of stock in store but can be shipped to you from another location.</p>
      <p><span class="marker">d.</span>Eligible to purchase exclusive items offered to members only. Purchasing of exclusive items is limited to 1 item per member per 30 days. Please see stores for details.</p>
    </div>
    <h2 class="display join-title">Join Today</h2>
    <ul class="signup">
      <li><span class="field-name">Your Name:</span><span class="field-line"></span></li>
      <li><span class="field-name">Phone Number:</span><span class="field-line"></span></li>
      <li><span class="field-name">Email Address:</span><span class="field-line"></span></li>
    </ul>
    <div class="social">
      <div class="social__cta">click like follow</div>
      <div>www.zstridashop.example</div>
    </div>
    <div class="social__networks">Linkbook<br>Chirpline</div>
  </section>
</main>
</body>
</html>
```